Bookkeeping business needs a digital and print flyer

We need a flyer to promote our virtual bookkeeping services to small and mid-sized businesses in the United States. We want the content and design of the flyer to be consistent with our website: www.brightlanebookkeeping.example. We would like both a print version and a digital version of the flyer.

```html
<!DOCTYPE html>
<html lang="en">
<head>
<meta charset="utf-8">
<title>Bright Lane Bookkeeping Flyer</title>
<link href="https://fonts.googleapis.com/css2?family=Poppins:ital,wght@0,300;0,400;0,600;0,700;1,500;1,700&display=swap" rel="stylesheet">
<style>
  :root {
    --navy: #2c2d55;
    --navy-deep: #12143f;
    --ink: #151845;
    --gold: #f2c20f;
    --paper: #f1f1f1;
    --panel: #e9e9ea;
    --stage: #8aa7a5;
  }
  * { box-sizing: border-box; margin: 0; padding: 0; }
  html, body { width: 1200px; height: 1117px; overflow: hidden; }
  body { background: var(--stage); font-family: 'Poppins', sans-serif; color: var(--ink); }
  .flyer {
    position: absolute; left: 220px; top: 20px; width: 760px; height: 1077px;
    background: var(--paper); overflow: hidden;
  }
  .hero { position: absolute; left: 0; top: 0; width: 760px; height: 412px; background: var(--navy); }
  .photo-frame {
    position: absolute; left: 385px; top: 0; width: 375px; height: 338px;
    background: var(--gold); border-bottom-left-radius: 60px;
  }
  .photo-frame .edge {
    position: absolute; left: 14px; top: 0; right: 0; bottom: 14px;
    background: var(--navy-deep); border-bottom-left-radius: 48px;
  }
  .photo {
    position: absolute; left: 19px; top: 0; right: 0; bottom: 19px;
    border-bottom-left-radius: 44px;
    background: linear-gradient(135deg, #e8ece6 0%, #c9cfc8 40%, #8aa0b8 75%, #6b7f96 100%);
  }
  .brand { position: absolute; left: 74px; top: 46px; display: flex; align-items: center; gap: 12px; }
  .brand-name { color: #fff; font-weight: 300; font-size: 29px; line-height: 1; letter-spacing: 1px; text-align: right; }
  .brand-name small { display: block; font-size: 13px; letter-spacing: 1.5px; margin-top: 4px; }
  .brand-dot { width: 48px; height: 48px; border: 3px solid #fff; border-radius: 50%; }
  .headline {
    position: absolute; left: 70px; top: 124px; font-weight: 700; font-size: 43px;
    line-height: 44.5px; color: #fff;
  }
  .headline .accent { color: var(--gold); }
  .tagline { position: absolute; left: 100px; top: 362px; color: #fff; font-size: 21px; }
  .tagline em { color: var(--gold); font-style: italic; font-weight: 500; }
  .hello {
    position: absolute; left: 68px; top: 434px; width: 624px; height: 49px;
    border: 2px solid var(--gold); border-radius: 6px; display: flex; align-items: center; justify-content: center;
    font-weight: 700; font-size: 19.5px; color: var(--ink);
  }
  .needs-panel {
    position: absolute; left: 379px; top: 500px; width: 381px; height: 437px;
    background: var(--panel); border-top-left-radius: 26px;
  }
  .col-title {
    position: absolute; font-weight: 700; font-size: 20px; line-height: 24px; text-align: center;
    color: var(--ink); padding-bottom: 12px; border-bottom: 1.5px solid var(--gold);
  }
  .benefits-title { left: 68px; top: 520px; width: 266px; }
  .needs-title { left: 425px; top: 523px; width: 266px; }
  .benefits { position: absolute; left: 68px; top: 594px; width: 290px; list-style: none; }
  .benefits li {
    position: relative; padding-left: 23px; font-size: 13.6px; line-height: 16px; margin-bottom: 12px;
  }
  .benefits li svg { position: absolute; left: 0; top: 2px; }
  .benefits li b { display: block; font-style: italic; font-weight: 700; }
  .needs { position: absolute; left: 425px; top: 594px; width: 270px; list-style: none; }
  .needs li { position: relative; padding-left: 17px; font-size: 12.6px; line-height: 15px; margin-bottom: 8.5px; }
  .needs li::before {
    content: ""; position: absolute; left: 0; top: 6px; width: 4px; height: 4px; border-radius: 50%;
    background: var(--ink);
  }
  .closing {
    position: absolute; left: 0; top: 937px; width: 760px; height: 140px; background: var(--navy-deep);
  }
  .closing p {
    position: absolute; left: 0; width: 760px; top: 22px; text-align: center; color: #fff;
    font-weight: 700; font-size: 22px;
  }
  .closing p span { color: var(--gold); }
  .contact-bar {
    position: absolute; left: 0; top: 1009px; width: 730px; height: 68px; background: var(--gold);
    border-top-right-radius: 26px; display: flex; align-items: center; justify-content: center; gap: 14px;
    font-weight: 600; font-size: 13px; color: var(--ink); padding-top: 4px;
  }
  .contact-bar span { display: flex; align-items: center; gap: 5px; }
</style>
</head>
<body>
<main class="flyer">
  <section class="hero">
    <div class="brand">
      <div class="brand-name">BRIGHT LANE<small>BOOKKEEPING</small></div>
      <div class="brand-dot"></div>
    </div>
    <h1 class="headline"><span class="accent">Virtual<br>Bookkeeping</span><br>for Small and<br>mid-sized<br>businesses</h1>
    <div class="photo-frame">
      <div class="edge"></div>
      <div class="photo" role="img" aria-label="Photo of two colleagues reviewing finances together on a laptop"></div>
    </div>
    <p class="tagline">Build Your Business by <em>Focusing on What You Love</em></p>
  </section>

  <div class="hello">Say Hello to a reliable, hassle-free bookkeeping solution!</div>

  <div class="needs-panel"></div>

  <h2 class="col-title benefits-title">What you get with Bright Lane Bookkeeping</h2>
  <ul class="benefits">
    <li><svg width="12" height="12" viewBox="0 0 12 12"><circle cx="6" cy="6" r="6" fill="#f2c20f"/><path d="M3.3 6.2l1.8 1.8 3.6-3.7" stroke="#fff" stroke-width="1.5" fill="none"/></svg>Worry no more about finding time and energy to tackle bookkeeping<b>– Hakuna Matata!</b></li>
    <li><svg width="12" height="12" viewBox="0 0 12 12"><circle cx="6" cy="6" r="6" fill="#f2c20f"/><path d="M3.3 6.2l1.8 1.8 3.6-3.7" stroke="#fff" stroke-width="1.5" fill="none"/></svg>Keep more of your hard-earned money by maximizing tax deductions<b>– Ka-Ching!</b></li>
    <li><svg width="12" height="12" viewBox="0 0 12 12"><circle cx="6" cy="6" r="6" fill="#f2c20f"/><path d="M3.3 6.2l1.8 1.8 3.6-3.7" stroke="#fff" stroke-width="1.5" fill="none"/></svg>Understand those confusing financial reports to take your business to the next level<b>– Booyah!</b></li>
    <li><svg width="12" height="12" viewBox="0 0 12 12"><circle cx="6" cy="6" r="6" fill="#f2c20f"/><path d="M3.3 6.2l1.8 1.8 3.6-3.7" stroke="#fff" stroke-width="1.5" fill="none"/></svg>Celebrate each month’s wins during monthly consultations<b>–Hooray!</b></li>
    <li><svg width="12" height="12" viewBox="0 0 12 12"><circle cx="6" cy="6" r="6" fill="#f2c20f"/><path d="M3.3 6.2l1.8 1.8 3.6-3.7" stroke="#fff" stroke-width="1.5" fill="none"/></svg>Stress-free tax time<b>– Oh Yeah!</b></li>
  </ul>

  <h2 class="col-title needs-title">Bookkeeping Tailored to YOUR Business Needs</h2>
  <ul class="needs">
    <li>Catch-up and clean-up services</li>
    <li>Transaction importation and categorization</li>
    <li>Monthly reconciliation of all accounts, including assets and loans.</li>
    <li>Monthly financial reports (Balance Sheet, Income Statement, Cash Flow)</li>
    <li>Monthly video conference</li>
    <li>Annual tax-prep package sent to your preparer</li>
    <li>A/R &amp; A/P</li>
    <li>Payroll coordination</li>
    <li>1099s</li>
    <li>Bill pay and receipt management</li>
    <li>Budgeting</li>
  </ul>

  <footer class="closing">
    <p>Take bookkeeping off your <span>'To Do List' for good!</span></p>
  </footer>
  <div class="contact-bar">
    <span><svg width="14" height="14" viewBox="0 0 14 14"><circle cx="7" cy="7" r="7" fill="#151845"/><path d="M4.5 3.5l1.5 0 .6 1.8-.9.7a5 5 0 0 0 2.3 2.3l.7-.9 1.8.6v1.5c-3.5.3-6.3-2.5-6-6z" fill="#f2c20f"/></svg>555-014-2290</span>
    <span><svg width="14" height="14" viewBox="0 0 14 14"><circle cx="7" cy="7" r="7" fill="#151845"/><rect x="3.5" y="4.5" width="7" height="5" fill="none" stroke="#f2c20f" stroke-width="1"/><path d="M3.5 4.5l3.5 3 3.5-3" fill="none" stroke="#f2c20f" stroke-width="1"/></svg>maria@brightlanebookkeeping.example</span>
    <span><svg width="14" height="14" viewBox="0 0 14 14"><circle cx="7" cy="7" r="7" fill="#151845"/><circle cx="7" cy="7" r="3.8" fill="none" stroke="#f2c20f" stroke-width="1"/><path d="M3.2 7h7.6M7 3.2c-2 2.4-2 5.2 0 7.6M7 3.2c2 2.4 2 5.2 0 7.6" fill="none" stroke="#f2c20f" stroke-width="0.9"/></svg>www.brightlanebookkeeping.example</span>
  </div>
</main>
</body>
</html>
```